Villa Sereno needs a new website for its boutique apartment

We are a boutique apartment in Florence that rents out to tourists. We are looking to redesign our website. See the existing site at www.villaserenostay.example

Ideally redesigned site would enable us to easily add and change photos in the gallery and across the site.

The new logo for the apartment is currently under design but being based around the current house logo with a person standing inside.
Updates

Project Deadline Extended
Reason: The website design by the 1st Place designer has been long and drawn out and not led to the design that we were looking for. As such, we are extending the deadline for another 5 days to hopefully get new designs and options.

Target Market(s)

Global tourists

Industry/Entity Type

Accommodation

Coding

Coded - Design and coding required

Number of Pages Required

5+ page

Font styles to use
Sans Serif

Requirements
Must have
• Welcome page, gallery page, information page about apartment and availability page with link to booking sites. And option for another page with tourist information. We must be able to change the photos in the gallery with relative ease when required.
• The Villa Sereno font has been uploaded which is used with the logo and the new logo has been uploaded.
Nice to have
• Looking like a fun but professional hotel site
• Page info is located on www.villaserenostay.example site

```html
<!DOCTYPE html>
<html lang="en">
<head>
<meta charset="utf-8">
<title>Villa Sereno – Holiday Apartments in Florence</title>
<link href="https://fonts.googleapis.com/css2?family=Open+Sans:wght@400;600;700&family=Raleway:wght@400;500&display=swap" rel="stylesheet">
<style>
:root{
  --ink:#111111;
  --black:#000000;
  --white:#ffffff;
  --text:#222222;
  --muted:#444444;
  --rule:#d6d6d6;
  --panel:#e8e8e8;
  --overlay:rgba(12,14,16,.82);
  --hero-a:#c9b9a3;
  --hero-b:#6b5a48;
  --gallery-a:#2e3a3c;
  --gallery-b:#4a4f4e;
}
*{box-sizing:border-box;margin:0;padding:0}
html,body{width:1200px;height:2329px;overflow:hidden}
body{position:relative;background:var(--white);font-family:'Raleway',sans-serif;color:var(--text)}
.abs{position:absolute}

/* top bar */
.topbar{left:0;top:0;width:1200px;height:42px;background:var(--black);color:var(--white);font-family:'Open Sans',sans-serif}
.topbar .tagline{left:80px;top:11px;font-size:15px;font-weight:700}
.topbar .contact{top:11px;font-size:15px;display:flex;align-items:center;gap:12px}
.topbar .phone{left:500px}
.topbar .mail{left:697px}
.topbar .book{left:1009px;top:5px;width:104px;height:32px;border:1.5px solid var(--white);font-size:15px;text-align:center;line-height:29px}

/* header */
.header{left:0;top:42px;width:1200px;height:99px;background:var(--white)}
.brand{left:86px;top:35px;display:flex;align-items:center;gap:10px;font-size:24px;font-weight:500;color:var(--ink)}
.brand .mark{width:18px;height:18px;background:var(--ink)}
.nav{top:28px;font-size:18px;color:var(--ink);letter-spacing:.3px}
.nav.active{left:416px;width:93px;height:42px;top:28px;background:var(--ink);color:var(--white);text-align:center;line-height:42px}
.nav.n2{left:540px;line-height:42px}
.nav.n3{left:683px;line-height:42px}
.nav.n4{left:813px;line-height:42px}
.nav.n5{left:981px;line-height:42px}

/* hero */
.hero{left:0;top:141px;width:1200px;height:573px;background:linear-gradient(160deg,var(--hero-a) 0%,#a89580 45%,var(--hero-b) 100%)}
.search{left:0;top:624px;width:1200px;height:90px;background:var(--overlay);color:var(--white)}
.field-label{top:17px;font-size:14px}
.field{top:39px;height:31px;background:var(--white);color:var(--ink);font-size:15px;padding-left:8px;line-height:31px}
.field svg{position:absolute;right:8px;top:7px}
.spin{position:absolute;right:0;top:0;width:31px;height:31px;border-left:1px solid #999}
.search-btn{left:944px;top:39px;width:104px;height:31px;background:var(--white);color:var(--ink);font-size:17px;text-align:center;line-height:31px}

/* features */
.feature{top:744px;width:180px;text-align:center;font-size:16px;color:var(--muted)}
.feature svg{display:block;margin:0 auto 10px}
.divider{left:78px;top:846px;width:1044px;height:1px;background:var(--rule)}

/* welcome */
.welcome-title{left:0;top:872px;width:1200px;text-align:center;font-size:44px;font-weight:400;color:var(--ink)}
.welcome-text{left:160px;top:965px;width:880px;text-align:center;font-size:15.5px;line-height:33px;color:var(--text)}

/* gallery */
.gallery{left:0;top:1164px;width:1200px;height:729px;background:radial-gradient(ellipse at 50% 40%,var(--gallery-b),var(--gallery-a) 75%)}
.gallery-title{left:0;top:1209px;width:1200px;text-align:center;font-size:44px;color:var(--white)}
.thumb{width:334px;height:208px;border:2px solid var(--white)}
.t1{left:78px;top:1307px;background:linear-gradient(135deg,#d9cfc2,#b8a48a)}
.t2{left:433px;top:1307px;background:linear-gradient(135deg,#6a6d70,#8a8c8e)}
.t3{left:789px;top:1307px;background:linear-gradient(135deg,#cfc8bd,#8c7e6c)}
.t4{left:78px;top:1557px;background:linear-gradient(135deg,#b49a6d,#e4dfd6)}
.t5{left:433px;top:1557px;background:linear-gradient(135deg,#c8b08a,#6f5c44)}
.t6{left:789px;top:1557px;background:linear-gradient(135deg,#e0ddd7,#3b4a6b)}
.thumb .zoom{position:absolute;left:50%;top:50%;transform:translate(-50%,-50%)}
.view-all{left:528px;top:1815px;width:144px;height:42px;border:1.5px solid var(--white);color:var(--white);font-size:17px;text-align:center;line-height:39px}

/* why */
.why{left:0;top:1893px;width:1200px;height:378px;background:var(--panel)}
.why-title{left:102px;top:1928px;font-size:44px;color:var(--ink)}
.why-list{left:100px;top:2020px;list-style:none;font-size:16px;color:var(--text)}
.why-list li{height:31.5px;display:flex;align-items:center;gap:12px}
.check-btn{left:101px;top:2190px;width:219px;height:43px;border:1.5px solid var(--ink);font-size:18px;text-align:center;line-height:40px;color:var(--ink)}
.map{left:685px;top:1930px;width:417px;height:292px;border:2px solid var(--black);background:linear-gradient(135deg,#e8e6e0,#d8e0d2 50%,#ece8dd)}

/* footer */
.footer{left:0;top:2271px;width:1200px;height:58px;background:var(--black);color:var(--white);font-family:'Open Sans',sans-serif}
.footer .copy{left:81px;top:19px;font-size:15px}
.footer .copy b{font-weight:700}
.social{top:12px;width:34px;height:34px;border-radius:50%;background:var(--white)}
</style>
</head>
<body>

<div class="abs topbar">
  <div class="abs tagline">Holiday Apartments in Florence</div>
  <div class="abs contact phone">
    <svg width="18" height="18" viewBox="0 0 24 24"><path fill="#fff" d="M6.6 10.8a15.1 15.1 0 0 0 6.6 6.6l2.2-2.2c.3-.3.7-.4 1-.2 1.1.4 2.3.6 3.6.6.6 0 1 .4 1 1V20c0 .6-.4 1-1 1A17 17 0 0 1 3 4c0-.6.4-1 1-1h3.5c.6 0 1 .4 1 1 0 1.3.2 2.5.6 3.6.1.3 0 .7-.2 1z"/></svg>
    <span>39 300 555 0142</span>
  </div>
  <div class="abs contact mail">
    <svg width="20" height="16" viewBox="0 0 20 16"><rect x="1" y="1" width="18" height="14" fill="none" stroke="#fff" stroke-width="1.8"/><path d="M1 2l9 7 9-7" fill="none" stroke="#fff" stroke-width="1.8"/></svg>
    <span>reservations@villaserenostay.example</span>
  </div>
  <div class="abs book">Book Now</div>
</div>

<header class="abs header">
  <div class="abs brand"><span class="mark"></span>Villa Sereno</div>
  <div class="abs nav active">HOME</div>
  <div class="abs nav n2">ABOUT US</div>
  <div class="abs nav n3">GALLERY</div>
  <div class="abs nav n4">CONTECT US</div>
  <div class="abs nav n5">AVAILABILITY</div>
</header>

<div class="abs hero" role="img" aria-label="Photo of the apartment living room with sofa, table and tulips"></div>

<div class="abs search">
  <div class="abs field-label" style="left:155px">Check In</div>
  <div class="abs field" style="left:152px;width:230px">DD MM YYYY
    <svg width="16" height="16" viewBox="0 0 16 16"><rect x="1" y="3" width="14" height="12" fill="none" stroke="#333" stroke-width="1.4"/><path d="M1 6h14M5 1v4M11 1v4M4 9h2M7 9h2M10 9h2M4 12h2M7 12h2M10 12h2" stroke="#333" stroke-width="1.2"/></svg>
  </div>
  <div class="abs field-label" style="left:425px">Check Out</div>
  <div class="abs field" style="left:422px;width:230px">DD MM YYYY
    <svg width="16" height="16" viewBox="0 0 16 16"><rect x="1" y="3" width="14" height="12" fill="none" stroke="#333" stroke-width="1.4"/><path d="M1 6h14M5 1v4M11 1v4M4 9h2M7 9h2M10 9h2M4 12h2M7 12h2M10 12h2" stroke="#333" stroke-width="1.2"/></svg>
  </div>
  <div class="abs field-label" style="left:697px">Adults</div>
  <div class="abs field" style="left:694px;width:93px;padding-left:22px">1
    <span class="spin"><svg width="31" height="31" viewBox="0 0 31 31" style="position:static"><path d="M11 12l4.5-5 4.5 5M11 19l4.5 5 4.5-5" fill="none" stroke="#222" stroke-width="1.6"/><path d="M0 15.5h31" stroke="#999"/></svg></span>
  </div>
  <div class="abs field-label" style="left:821px">Kids</div>
  <div class="abs field" style="left:818px;width:93px;padding-left:22px">1
    <span class="spin"><svg width="31" height="31" viewBox="0 0 31 31" style="position:static"><path d="M11 12l4.5-5 4.5 5M11 19l4.5 5 4.5-5" fill="none" stroke="#222" stroke-width="1.6"/><path d="M0 15.5h31" stroke="#999"/></svg></span>
  </div>
  <div class="abs search-btn">SEARCH</div>
</div>

<div class="abs feature" style="left:90px">
  <svg width="40" height="36" viewBox="0 0 40 36"><path d="M4 14a23 23 0 0 1 32 0M9 19a16 16 0 0 1 22 0M14 24a9 9 0 0 1 12 0" fill="none" stroke="#333" stroke-width="1.6"/><circle cx="20" cy="29" r="2" fill="#333"/></svg>
  Free WiFi
</div>
<div class="abs feature" style="left:301px">
  <svg width="40" height="36" viewBox="0 0 40 36"><path d="M12 3h16l3 15H9z M20 18v12 M14 32h12" fill="none" stroke="#333" stroke-width="1.6"/></svg>
  Fully Furnished
</div>
<div class="abs feature" style="left:509px">
  <svg width="40" height="36" viewBox="0 0 40 36"><circle cx="20" cy="18" r="16" fill="none" stroke="#333" stroke-width="1.6"/><path d="M16 27V10h6a4.5 4.5 0 0 1 0 9h-6" fill="none" stroke="#333" stroke-width="1.8"/></svg>
  Free Parking
</div>
<div class="abs feature" style="left:720px">
  <svg width="40" height="36" viewBox="0 0 40 36"><path d="M30 4l4 2-8 10 3 12-3 2-6-10-6 6 1 5-2 1-3-6-6-3 1-2 5 1 6-6-10-6 2-3 12 3z" fill="none" stroke="#333" stroke-width="1.5" stroke-linejoin="round"/></svg>
  Airport Transfers
</div>
<div class="abs feature" style="left:928px">
  <svg width="40" height="36" viewBox="0 0 40 36"><path d="M32 2L20 18M14 16l8 8-6 10-10-14z M10 22l6 8M12 19l7 9" fill="none" stroke="#333" stroke-width="1.5" stroke-linejoin="round"/></svg>
  Cleaning Services
</div>
<div class="abs divider"></div>

<h1 class="abs welcome-title">Welcome to Villa Sereno</h1>
<p class="abs welcome-text">"Villa Sereno" is a newly renovated boutique 2-bedroom loft apartment in the historic centre of Florence (Firenze), Italy. "Villa Sereno" is perfectly located for your Tuscan holiday, offering easy walking access to all of central Florence - only 600m from the Duomo and Ponte Vecchio. The apartment is configured to sleep up to six and is furnished with elegant and luxury fittings, and has complimentary high-speed internet and cable-TV.</p>

<section class="abs gallery" role="img" aria-label="Blurred background photo of bathroom toiletries"></section>
<h2 class="abs gallery-title">Our Gallery</h2>
<div class="abs thumb t1" role="img" aria-label="Photo of open-plan kitchen and dining area with staircase"></div>
<div class="abs thumb t2" role="img" aria-label="Photo of bedroom with white bedding">
  <svg class="zoom" width="34" height="34" viewBox="0 0 34 34"><circle cx="14" cy="14" r="9.5" fill="none" stroke="#fff" stroke-width="4"/><path d="M21 21l9 9" stroke="#fff" stroke-width="5" stroke-linecap="round"/></svg>
</div>
<div class="abs thumb t3" role="img" aria-label="Photo of modern kitchen with tulips on the table"></div>
<div class="abs thumb t4" role="img" aria-label="Photo of armchair and bedroom view"></div>
<div class="abs thumb t5" role="img" aria-label="Photo of loft reading corner with floor lamp"></div>
<div class="abs thumb t6" role="img" aria-label="Photo of bedroom with blue bedding under a window"></div>
<div class="abs view-all">VIEW ALL</div>

<section class="abs why"></section>
<h2 class="abs why-title">Why book with us</h2>
<ul class="abs why-list">
  <li><svg width="16" height="14" viewBox="0 0 16 14"><path d="M8 0L0 7h2v7h4.5V9.5h3V14H14V7h2z" fill="#111"/></svg>Nearest Airport 8 Kilometres Florence Airport (FLR)</li>
  <li><svg width="16" height="14" viewBox="0 0 16 14"><path d="M8 0L0 7h2v7h4.5V9.5h3V14H14V7h2z" fill="#111"/></svg>Nearest Beach 100 Kilometres Via Reggio</li>
  <li><svg width="16" height="14" viewBox="0 0 16 14"><path d="M8 0L0 7h2v7h4.5V9.5h3V14H14V7h2z" fill="#111"/></svg>Nearest Train 600 Metres Santa Maria Novella</li>
  <li><svg width="16" height="14" viewBox="0 0 16 14"><path d="M8 0L0 7h2v7h4.5V9.5h3V14H14V7h2z" fill="#111"/></svg>Private parking in the same building</li>
  <li><svg width="16" height="14" viewBox="0 0 16 14"><path d="M8 0L0 7h2v7h4.5V9.5h3V14H14V7h2z" fill="#111"/></svg>Solarium and terrace on the roof</li>
</ul>
<div class="abs check-btn">CHECK AVAILABILITY</div>
<div class="abs map" role="img" aria-label="Street map of central Florence showing the apartment location"></div>

<footer class="abs footer">
  <div class="abs copy">© <b>Villa Sereno</b> - 2016. All Rights Reserved.</div>
  <div class="abs social" style="left:922px"></div>
  <div class="abs social" style="left:977px"></div>
  <div class="abs social" style="left:1026px"></div>
  <div class="abs social" style="left:1077px"></div>
</footer>

</body>
</html>
```